A mobile coffee, eats and treats van. We sell freshly ground Valtorino coffee, a selection of yummy things to eats, and lovely giftwares, including candles, scarfs, jewellery. We also have an online store where additional home and giftwares can be purchased

Thanks so much for all your efforts so far, I have received some great concepts.  Just wanted to send out a reminder that our concept is coffee, eats and treats (the treats being home and gift ware)  We have a mobile van and also an online store.  I dont want to make my business card too "busy" but at the same time I would like to give my potential customers something that will really excite and intrigue them...

Reason: Its the weekend....have a break!

Thank you everyone for your designs...I think I have made a decision...have just sent out a couple of questions.  I will be loading a new project shortly if you are interested?  Thanks, Marlene

Store

The Dusky Wren - Coffee, Eats & Treats
Marlene Quistorff
0459 863 205
marlene@theduskywren.com.au
www.theduskywren.com.au
www.facebook.com/theduskywren
https://twitter.com/TheDuskyWren

• It would be good to have a rewards program on the back, we can tick off when prople buy coffee....5th coffee free...something like that...

It would also be good for the card to look like a gift tag....

```html
<!DOCTYPE html>
<html lang="en">
<head>
<meta charset="utf-8">
<title>The Dusky Wren – Business &amp; Rewards Cards</title>
<link rel="stylesheet" href="https://fonts.googleapis.com/css2?family=Montserrat:wght@800&family=Questrial&display=swap">
<style>
  :root {
    --canvas: #e9e6df;
    --espresso: #3b3322;
    --latte-gold: #b3a275;
    --milk: #ffffff;
    --card-shadow: rgba(40, 32, 20, 0.22);
  }
  * { box-sizing: border-box; margin: 0; padding: 0; }
  html, body {
    width: 1200px; height: 900px; overflow: hidden;
    background: var(--canvas);
  }
  .canvas { position: relative; width: 1200px; height: 900px; }

  .card {
    position: absolute;
    width: 520px; height: 316px;
    border-radius: 18px;
    overflow: hidden;
    box-shadow: 0 8px 22px var(--card-shadow);
  }
  .brand-name {
    font-family: "Montserrat", sans-serif;
    font-weight: 800;
    letter-spacing: -1px;
    line-height: 1;
    white-space: nowrap;
  }
  .tagline {
    font-family: "Questrial", sans-serif;
    font-size: 21px;
    letter-spacing: 0.3px;
    white-space: nowrap;
  }

  /* Rewards card */
  .rewards-card {
    left: 290px; top: 80px;
    background: var(--espresso);
    color: var(--milk);
  }
  .rewards-card .brand-name {
    position: absolute; left: 70px; top: 72px;
    font-size: 46px; color: var(--milk);
  }
  .rewards-card .tagline {
    position: absolute; right: 66px; top: 126px;
    color: var(--milk);
  }
  .stamp-row {
    position: absolute; left: 124px; top: 172px;
    display: flex; gap: 13px;
  }
  .stamp {
    width: 52px; height: 52px; border-radius: 50%;
    background: var(--milk);
  }
  .stamp--free { display: flex; align-items: center; justify-content: center; }
  .social-row {
    position: absolute; right: 62px; bottom: 36px;
    display: flex; gap: 18px;
    font-family: "Questrial", sans-serif;
    font-size: 15px; letter-spacing: 0.8px;
    color: var(--latte-gold);
  }
  .social-handle { display: flex; align-items: center; gap: 7px; }
  .social-square {
    width: 15px; height: 15px; border-radius: 2px;
    background: var(--latte-gold);
  }

  /* Contact card */
  .contact-card {
    left: 350px; top: 480px;
    background: var(--milk);
  }
  .contact-card .wave { position: absolute; inset: 0; }
  .contact-card .brand-name {
    position: absolute; left: 92px; top: 78px;
    font-size: 52px; color: var(--espresso);
  }
  .contact-card .tagline {
    position: absolute; right: 42px; top: 138px;
    font-size: 22px; color: var(--espresso);
  }
  .contact-details {
    position: absolute; left: 44px; top: 204px;
    font-family: "Questrial", sans-serif;
    color: var(--milk);
    line-height: 1.35;
  }
  .contact-name { font-size: 18px; letter-spacing: 0.4px; margin-bottom: 6px; }
  .contact-line { font-size: 13px; letter-spacing: 0.3px; }
</style>
</head>
<body>
<main class="canvas">

  <section class="card rewards-card" aria-label="Coffee rewards card">
    <h2 class="brand-name">the dusky wren</h2>
    <p class="tagline">coffee, eats &amp; treats</p>
    <div class="stamp-row">
      <span class="stamp"></span>
      <span class="stamp"></span>
      <span class="stamp"></span>
      <span class="stamp"></span>
      <span class="stamp stamp--free" aria-label="Fifth coffee free">
        <svg width="34" height="26" viewBox="0 0 34 26" aria-hidden="true">
          <path d="M3 6 H25 V14 A11 10 0 0 1 3 14 Z" fill="#3b3322"/>
          <path d="M25 8 h3 a4 4 0 0 1 0 8 h-4" fill="none" stroke="#3b3322" stroke-width="2.4"/>
          <ellipse cx="14" cy="6" rx="11" ry="2.6" fill="#b3a275"/>
          <rect x="1" y="23" width="26" height="2" rx="1" fill="#3b3322"/>
        </svg>
      </span>
    </div>
    <div class="social-row">
      <span class="social-handle"><span class="social-square"></span>theduskywren</span>
      <span class="social-handle"><span class="social-square"></span>TheDuskyWren</span>
    </div>
  </section>

  <section class="card contact-card" aria-label="Business card">
    <svg class="wave" viewBox="0 0 520 316" preserveAspectRatio="none" aria-hidden="true">
      <path d="M0 176 C110 164 230 180 320 212 C390 236 450 236 520 222 V316 H0 Z" fill="#b3a275"/>
      <path d="M0 186 C110 176 230 192 318 222 C388 246 450 246 520 232 V316 H0 Z" fill="#3b3322"/>
    </svg>
    <h2 class="brand-name">the dusky wren</h2>
    <p class="tagline">coffee, eats &amp; treats</p>
    <address class="contact-details" style="font-style: normal;">
      <p class="contact-name">Marlene Quistorff</p>
      <p class="contact-line">0459 863 205</p>
      <p class="contact-line">marlene@theduskywren.com.au</p>
      <p class="contact-line">www.theduskywren.com.au</p>
    </address>
  </section>

</main>
</body>
</html>
```